Power menders . Energy efficiency improvement for residential and commercial/industrial

Logo needed for “ power menders .com “ website. Conduct energy audits and provide consulting about efficiency improvements . I will provide content for pages about 10 pages . Get customer serway and store information .
Some pages will be copied from Gridpulsera.com

```html
<!DOCTYPE html>
<html lang="en">
<head>
<meta charset="utf-8">
<title>Power menders</title>
<link href="https://fonts.googleapis.com/css2?family=Rubik:wght@400;500;700&family=Saira+Semi+Condensed:wght@600;700&display=swap" rel="stylesheet">
<style>
:root{
  --blue:#0b5fd0;
  --blue-deep:#0a3f8f;
  --navy:#071a3d;
  --orange:#ec9a28;
  --orange-dark:#e08a12;
  --ink:#1d1d1d;
  --white:#ffffff;
  --footer:#262626;
  --footer-line:#8a7a3c;
}
*{margin:0;padding:0;box-sizing:border-box}
html,body{width:1200px;height:4511px;overflow:hidden;background:var(--white)}
body{font-family:"Rubik",sans-serif;color:var(--ink);position:relative}
.page{position:relative;width:1200px;height:4511px;overflow:hidden}
.abs{position:absolute}
.heading{font-family:"Saira Semi Condensed",sans-serif;font-weight:700;letter-spacing:.5px}
.btn{position:absolute;display:flex;align-items:center;gap:12px;background:var(--blue);color:var(--white);font-size:13px;font-weight:500;letter-spacing:.6px;padding:0 20px;height:40px;border-radius:3px}
.btn .dot{width:14px;height:14px;border-radius:50%;background:var(--white);display:flex;align-items:center;justify-content:center}
.btn .dot::after{content:"";border-left:5px solid var(--blue);border-top:3.5px solid transparent;border-bottom:3.5px solid transparent;margin-left:2px}
.brand{display:flex;align-items:center;gap:12px;color:var(--white)}
.brand .mark{width:48px;height:48px;border-radius:50%;background:var(--white)}
.brand .name{font-family:"Rubik",sans-serif;font-weight:700;font-size:25px;line-height:1;letter-spacing:1px}

/* hero */
.hero{left:0;top:0;width:1200px;height:720px;background:radial-gradient(ellipse at 50% 70%,#1d4f9a 0%,#0b2a63 45%,var(--navy) 100%)}
.nav{position:absolute;top:40px;left:336px;display:flex;gap:34px;font-size:13px;font-weight:500;color:var(--white)}
.nav .active{color:#7fb3ff;border-bottom:2px solid #7fb3ff;padding-bottom:10px}
.hero-title{position:absolute;top:288px;width:1200px;text-align:center;color:var(--white);font-size:70px}
.hero .btn{left:517px;top:390px}
.arrow{position:absolute;top:330px;width:52px;height:52px;border:2px solid rgba(255,255,255,.6);border-radius:50%}
.dots{position:absolute;top:626px;left:577px;display:flex;gap:7px}
.dots span{width:8px;height:8px;border-radius:50%;border:1.5px solid #fff}
.dots span.on{background:var(--blue);border-color:var(--blue)}

.quote{top:782px;left:140px;width:920px;text-align:center;font-size:16px;font-weight:500;line-height:30px}
.divider{top:922px;left:110px;width:980px;height:1px;background:#8a9ab5}
.divider-knob{top:902px;left:580px;width:40px;height:40px;border-radius:50%;background:var(--blue)}

.img-fill{position:absolute}
.section-title{font-size:38px;color:var(--blue)}
.body-text{font-size:14px;line-height:24.5px}
.body-text p+p{margin-top:16px}

/* benefits */
.benefit-intro{top:1553px;left:110px;width:980px;text-align:center;color:var(--white);font-size:17.5px;line-height:31px}
.card{position:absolute;top:1664px;width:300px;height:394px;background:var(--white);border-radius:3px;padding:20px 16px}
.card .icon{width:98px;height:98px;border-radius:50%;background:var(--blue)}
.card h3{color:var(--orange);font-size:23px;line-height:28px;margin:18px 0 14px}
.card ul{list-style:none;font-size:13.5px;line-height:24.5px}
.card li{position:relative;padding-left:20px;margin-bottom:11px}
.card li::before{content:"";position:absolute;left:2px;top:9px;width:6px;height:6px;border-radius:50%;background:var(--blue)}

/* modern */
.modern-title{top:2700px;width:1200px;text-align:center;color:var(--white);font-size:40px}
.modern-intro{top:2768px;left:140px;width:920px;text-align:center;color:var(--white);font-size:16px;font-weight:500;line-height:28px}
.node{position:absolute;width:70px;height:70px;border-radius:50%;background:var(--orange)}
.node-label{position:absolute;color:var(--white);font-family:"Saira Semi Condensed",sans-serif;font-weight:700;font-size:18px;letter-spacing:.3px}
.hub{top:2980px;left:502px;width:196px;height:196px;border-radius:50%;background:var(--white);display:flex;align-items:center;justify-content:center}
.hub-inner{width:176px;height:176px;border-radius:50%;border:2px dashed var(--blue);display:flex;align-items:center;justify-content:center;gap:8px}
.hub-inner .mark{width:20px;height:20px;border-radius:50%;background:var(--blue)}
.hub-inner .name{color:var(--orange);font-weight:700;font-size:17px}
.btn-ghost{background:var(--white);color:var(--orange)}
.btn-ghost .dot{background:var(--orange)}
.btn-ghost .dot::after{border-left-color:var(--white)}

/* footer */
.footer{left:0;top:3960px;width:1200px;height:551px;background:var(--footer)}
.f-head{position:absolute;color:var(--white);font-family:"Saira Semi Condensed",sans-serif;font-weight:700;font-size:19px;letter-spacing:1px}
.f-head::after{content:"";display:block;width:40px;height:2px;background:var(--orange);margin-top:14px}
.f-list{position:absolute;list-style:none;color:#e6e6e6;font-size:13.5px;line-height:28px;font-weight:500}
.contact{position:absolute;color:#e6e6e6;font-size:14px;line-height:26px;display:flex;gap:18px}
.contact svg{flex:none;margin-top:5px}
.social{position:absolute;top:4326px;width:50px;height:50px;border-radius:50%;background:var(--blue)}
.f-rule{left:110px;top:4435px;width:980px;height:1px;background:var(--footer-line)}
.f-bottom{position:absolute;top:4460px;color:#e6e6e6;font-size:13px}
</style>
</head>
<body>
<div class="page">

  <!-- hero -->
  <section class="abs hero">
    <div class="img-fill" role="img" aria-label="Night city skyline beneath a glowing network of connected lines" style="inset:0;background:linear-gradient(180deg,rgba(20,40,90,.2),rgba(40,90,170,.35) 70%,rgba(7,26,61,.6))"></div>
    <div class="abs brand" style="left:50px;top:22px">
      <span class="mark"></span><span class="name">POWER MENDERS</span>
    </div>
    <nav class="nav">
      <span class="active">HOME</span><span>NEW FOR 2021</span><span>WHAT IS PM?</span><span>HOW PM WORKS</span><span>PM COST SAVINGS</span><span>CASE STUDIES</span><span>ABOUT</span>
    </nav>
    <h1 class="hero-title heading">POWER MENDERS</h1>
    <div class="btn">GET STARTED <span class="dot"></span></div>
    <div class="arrow" style="left:32px"><svg width="48" height="48" viewBox="0 0 48 48"><path d="M30 24H18M23 19l-5 5 5 5" stroke="#fff" stroke-width="2" fill="none"/></svg></div>
    <div class="arrow" style="left:1112px"><svg width="48" height="48" viewBox="0 0 48 48"><path d="M18 24h12M25 19l5 5-5 5" stroke="#fff" stroke-width="2" fill="none"/></svg></div>
    <div class="dots"><span class="on"></span><span></span><span></span><span></span></div>
    <svg class="abs" style="left:0;top:600px" width="1200" height="120" viewBox="0 0 1200 120">
      <polygon points="0,40 420,112 1200,22 1200,120 0,120" fill="#fff"/>
      <polygon points="0,40 420,112 0,68" fill="#0b5fd0"/>
    </svg>
  </section>

  <p class="abs quote">"Power menders Energy Management System was made for energy efficiency projects. It helps identify the best opportunities and creates the benchmarking, verification and ROI data to justify the projects and apply for the rebates!" &nbsp;— Energy Efficiency Engineer</p>
  <div class="abs divider"></div>
  <div class="abs divider-knob"><svg width="40" height="40" viewBox="0 0 40 40"><path d="M15 18l5 5 5-5" stroke="#fff" stroke-width="2" fill="none"/></svg></div>

  <!-- about -->
  <div class="img-fill" role="img" aria-label="Woman checking energy use on a tablet in a bright modern room" style="left:110px;top:1003px;width:472px;height:344px;background:linear-gradient(135deg,#d9d7d3,#f1efea 45%,#b7a596 80%,#6a4a34)"></div>
  <h2 class="abs heading section-title" style="left:612px;top:980px">ABOUT US</h2>
  <div class="abs body-text" style="left:612px;top:1040px;width:488px">
    <p>Power menders provides a unique Energy Monitoring, Operations Management, and Engineering Support solution using advanced wireless IoT technology to help companies understand and effectively manage energy use and equipment operations to achieve efficiency, reliability and sustainability.</p>
    <p>Energy monitoring in support of operational efficiency is essential for modern manufacturing and facility management. Power menders fully integrated energy &amp; operations management solution is not simply an expense, but a cost-reduction tool with many applications.</p>
  </div>
  <div class="btn" style="left:612px;top:1306px">LEARN MORE <span class="dot"></span></div>

  <!-- benefits -->
  <svg class="abs" style="left:0;top:1430px" width="1200" height="716" viewBox="0 0 1200 716">
    <polygon points="0,55 470,4 1200,60 1200,716 0,716" fill="#ec9a28"/>
    <polygon points="0,55 420,10 0,80" fill="#0b5fd0"/>
  </svg>
  <p class="abs benefit-intro">Specifically, Power menders lets you view the performance of your Production and HVAC equipment at multiple levels - i.e. a single machine, a production line, a production floor, an entire facility or multiple facilities - with the data visible on one dashboard. The main benefits are...</p>
  <div class="card" style="left:110px">
    <div class="icon"><svg width="98" height="98" viewBox="0 0 98 98"><circle cx="49" cy="49" r="30" stroke="#fff" stroke-width="2" fill="none"/><path d="M52 32l-10 19h9l-5 15 12-21h-9z" fill="#fff"/></svg></div>
    <h3 class="heading">ENERGY<br>SAVINGS</h3>
    <ul><li>Where and when is energy being wasted?</li><li>Track your largest energy-using machines and equipment</li><li>When and how is your Peak Demand usage set?</li></ul>
  </div>
  <div class="card" style="left:450px">
    <div class="icon"><svg width="98" height="98" viewBox="0 0 98 98"><circle cx="49" cy="49" r="30" stroke="#fff" stroke-width="2" fill="none"/><circle cx="49" cy="49" r="14" stroke="#fff" stroke-width="5" stroke-dasharray="5 4" fill="none"/><circle cx="49" cy="49" r="6" stroke="#fff" stroke-width="2" fill="none"/></svg></div>
    <h3 class="heading">OPERATING<br>EFFICIENCY</h3>
    <ul><li>Monitor critical machine-health</li><li>Track high-maintenance equipment</li><li>Optimize machine settings and processes</li></ul>
  </div>
  <div class="card" style="left:788px">
    <div class="icon"><svg width="98" height="98" viewBox="0 0 98 98"><circle cx="49" cy="49" r="30" stroke="#fff" stroke-width="2" fill="none"/><path d="M37 49l8 8 16-17" stroke="#fff" stroke-width="4" fill="none"/></svg></div>
    <h3 class="heading">RELIABILITY &amp;<br>SUSTAINABILITY</h3>
    <ul><li>Advance warning of machine failure avoids downtime</li><li>Benchmark/compare machine, production line, or process efficiency</li><li>Maintain equipment proactively</li></ul>
  </div>

  <!-- swiss knife -->
  <div class="abs body-text" style="left:110px;top:2236px;width:470px">
    <p>Power menders is the Swiss-Army-Knife of real-time equipment monitoring. It can save manufacturers a great deal in terms of energy-cost, machine-reliability, management time and improved maintenance.</p>
    <p>In many utility areas, rebates and incentives are offered for energy-reduction projects, which in most cases would pay for 50-100% of the capital cost of a complete Power menders</p>
  </div>
  <div class="btn" style="left:110px;top:2466px">LEARN MORE <span class="dot"></span></div>
  <div class="abs" style="left:613px;top:2390px;width:176px;height:172px;background:var(--orange)"></div>
  <div class="img-fill" role="img" aria-label="Earth at night seen from space, lit by blue data connections" style="left:631px;top:2233px;width:457px;height:313px;background:radial-gradient(ellipse at 70% 35%,#cfe6ff 0%,#3a8df0 18%,#0c3fa0 50%,#061844 100%)"></div>

  <!-- modern facility -->
  <svg class="abs" style="left:0;top:2630px" width="1200" height="830" viewBox="0 0 1200 830">
    <polygon points="0,0 1200,0 1200,740 760,820 0,745" fill="#0b5fd0"/>
    <polygon points="780,820 1200,740 1200,760" fill="#ec9a28"/>
  </svg>
  <h2 class="abs heading modern-title">MODERN FACILITY-MANAGEMENT AND MANUFACTURING</h2>
  <p class="abs modern-intro">Whether you have sustainability goals, efficiency targets, or sub-metering requirements (e.g. ISO 50001), modern operations for facility-management and manufacturing require economically-sound processes to minimize environmental impact while conserving energy and natural resources.</p>
  <svg class="abs" style="left:0;top:2900px" width="1200" height="360" viewBox="0 0 1200 360">
    <circle cx="600" cy="178" r="158" stroke="#9cc2f5" stroke-width="1.5" fill="none"/>
  </svg>
  <div class="abs hub"><div class="hub-inner"><span class="mark"></span><span class="name">POWER<br>MENDERS</span></div></div>
  <div class="node" style="left:454px;top:2914px"></div>
  <div class="node" style="left:664px;top:2914px"></div>
  <div class="node" style="left:396px;top:3043px"></div>
  <div class="node" style="left:724px;top:3043px"></div>
  <div class="node" style="left:464px;top:3176px"></div>
  <div class="node" style="left:654px;top:3176px"></div>
  <span class="node-label" style="left:248px;top:2918px">ENERGY PROCUREMENT</span>
  <span class="node-label" style="left:738px;top:2918px">DEMAND RESPONSE</span>
  <span class="node-label" style="left:172px;top:3066px">FACILITIES MANAGEMENT</span>
  <span class="node-label" style="left:804px;top:3066px">ENERGY EFFICIENCY</span>
  <span class="node-label" style="left:176px;top:3200px">MEASUREMENT &amp; VERIFICATION</span>
  <span class="node-label" style="left:738px;top:3200px">MACHINE MANAGEMENT</span>
  <div class="btn btn-ghost" style="left:517px;top:3296px">LEARN MORE <span class="dot"></span></div>

  <!-- company goals -->
  <div class="abs" style="left:93px;top:3521px;width:258px;height:210px;background:var(--orange)"></div>
  <div class="img-fill" role="img" aria-label="City skyline with glowing arcs of data linking buildings" style="left:110px;top:3539px;width:458px;height:358px;background:linear-gradient(180deg,#c7d3e3 0%,#8ea6c6 35%,#3d5f8c 70%,#1f3a63 100%)"></div>
  <h2 class="abs heading section-title" style="left:612px;top:3526px">YOUR COMPANY GOALS</h2>
  <div class="abs body-text" style="left:612px;top:3588px;width:488px">
    <p>Do your company goals include reducing waste, increasing operational efficiency, increasing competitive advantage, strengthening brand reputation and enhancing long-term business viability?</p>
    <p>Power menders provides the detailed data necessary to analyze and measure progress towards these goals.</p>
    <p>Specifically, Power menders answers key management questions, such as...</p>
  </div>
  <div class="btn" style="left:612px;top:3854px">LEARN MORE <span class="dot"></span></div>

  <!-- footer -->
  <footer class="abs footer">
    <svg class="abs" style="left:0;top:-2px" width="1200" height="90" viewBox="0 0 1200 90">
      <polygon points="0,0 1200,0 1200,2 0,2" fill="#fff"/>
      <polygon points="0,2 460,2 0,70" fill="#fff"/>
      <polygon points="0,44 460,0 0,70" fill="#0b5fd0"/>
    </svg>
  </footer>
  <div class="abs brand" style="left:90px;top:4178px"><span class="mark"></span><span class="name">POWER MENDERS</span></div>
  <div class="social" style="left:119px" role="img" aria-label="Social profile"></div>
  <div class="social" style="left:181px" role="img" aria-label="Social profile"></div>
  <div class="social" style="left:243px" role="img" aria-label="Social profile"></div>

  <h4 class="f-head" style="left:419px;top:4155px">CONTACT US</h4>
  <div class="contact" style="left:416px;top:4214px"><svg width="16" height="20" viewBox="0 0 16 20"><path d="M8 1a6 6 0 0 0-6 6c0 5 6 12 6 12s6-7 6-12a6 6 0 0 0-6-6z" fill="#fff"/><circle cx="8" cy="7" r="2.3" fill="#262626"/></svg><span>18 Harlow Street | Suite 310<br>Dunmore, Ohio 43210</span></div>
  <div class="contact" style="left:416px;top:4286px"><svg width="16" height="16" viewBox="0 0 16 16"><path d="M3 1l3 3-2 2c1 2 3 4 5 5l2-2 3 3-2 3C7 15 1 9 1 3z" fill="#fff"/></svg><span>555-014-2290</span></div>
  <div class="contact" style="left:414px;top:4326px"><svg width="20" height="16" viewBox="0 0 20 16"><rect x="5" y="1" width="10" height="5" fill="none" stroke="#fff" stroke-width="1.5"/><rect x="1" y="6" width="18" height="7" fill="none" stroke="#fff" stroke-width="1.5"/><rect x="5" y="10" width="10" height="5" fill="#fff"/></svg><span>555.014.7731</span></div>
  <div class="contact" style="left:414px;top:4370px"><svg width="20" height="14" viewBox="0 0 20 14"><rect x="1" y="1" width="18" height="12" fill="none" stroke="#fff" stroke-width="1.5"/><path d="M1 1l9 7 9-7" fill="none" stroke="#fff" stroke-width="1.5"/></svg><span>hello@powermenders.com</span></div>

  <h4 class="f-head" style="left:732px;top:4155px">QUICK LINKS</h4>
  <ul class="f-list" style="left:732px;top:4214px"><li>HOME</li><li>NEW FOR 2021</li><li>WHAT IS PM?</li><li>HOW PM WORKS</li><li>PM COST SAVINGS</li><li>CASE STUDIES</li><li>ABOUT</li></ul>
  <h4 class="f-head" style="left:954px;top:4155px">LINKS</h4>
  <ul class="f-list" style="left:954px;top:4214px"><li>FAQ'S</li><li>TERMS &amp; CONDITIONS</li><li>PRIVACY POLICY</li><li>SITE MAP</li></ul>

  <div class="abs f-rule"></div>
  <span class="f-bottom" style="left:110px">Copyright © 2021. &nbsp;All rights reserved</span>
  <span class="f-bottom" style="left:822px">Privacy Notice</span>
  <span class="abs" style="left:941px;top:4452px;width:1px;height:28px;background:var(--footer-line)"></span>
  <span class="f-bottom" style="left:966px">Conditions of Use</span>

</div>
</body>
</html>
```